Pike Hauling Business Card Design Project

We need a new company business card. We provide professional timber harvesting (logging) and forest management services. I'm open to any creative design. Most company caps and shirts are navy blue and Light grey. Logo does not necessarily have to contain those colors. Logo containing picture of logging equipment, log truck, trees, or logs are acceptable. Be creative. Final logo should communicate our company's pride and professionalism in the East Texas Timber Industry.
Updates

Target Market(s)

Timber owners, sawmills, and forestry professionals

Industry/Entity Type

Business

Requirements
Must have
• Must have Contact Info.
Phone: 936-402-5187
address: PO Box 8412
New Waverly, Tx 77358
www.rbpikehauling.example
rbpikehauling@mailbox.example
Owner: Pike Hauling

Or design must leave room for this info.

```html
<!DOCTYPE html>
<html lang="en">
<head>
<meta charset="utf-8">
<title>Pike Hauling – Business Card</title>
<link rel="stylesheet" href="https://fonts.googleapis.com/css2?family=Exo+2:wght@400;500;700&display=swap">
<style>
  :root {
    --backdrop: #d9d9d9;
    --card-white: #ffffff;
    --brand-red: #e32636;
    --swoosh-black: #231f20;
    --ink-dark: #231f20;
    --ink-light: #ffffff;
  }
  * { margin: 0; padding: 0; box-sizing: border-box; }
  html, body {
    width: 1200px; height: 771px; overflow: hidden;
    background: var(--backdrop);
    font-family: "Exo 2", Arial, sans-serif;
  }
  .canvas { position: relative; width: 1200px; height: 771px; }
  .business-card {
    position: absolute; left: 100px; top: 100px;
    width: 1000px; height: 572px;
    background: var(--card-white);
    overflow: hidden;
    box-shadow: 0 6px 20px rgba(0,0,0,0.18);
  }
  .card-shapes { position: absolute; inset: 0; width: 100%; height: 100%; }
  .contact-panel {
    position: absolute; left: 64px; top: 58px; width: 420px;
    color: var(--ink-light);
  }
  .person-name {
    font-size: 34px; font-weight: 500; letter-spacing: 3px;
    text-transform: uppercase;
  }
  .person-title { font-size: 19px; font-weight: 400; margin-top: 4px; letter-spacing: 0.5px; }
  .postal-address {
    font-style: normal; font-size: 19px; line-height: 1.4;
    margin-top: 40px; letter-spacing: 0.5px;
  }
  .contact-list { list-style: none; margin-top: 38px; }
  .contact-item {
    display: flex; align-items: center; gap: 14px;
    font-size: 18px; letter-spacing: 0.5px; margin-bottom: 12px;
  }
  .contact-icon { width: 20px; height: 20px; flex: none; fill: var(--ink-light); }
  .brand-lockup {
    position: absolute; left: 625px; top: 256px;
    display: flex; align-items: center; gap: 14px;
  }
  .brand-square { width: 26px; height: 26px; background: var(--brand-red); }
  .brand-name {
    font-size: 40px; font-weight: 700; color: var(--ink-dark);
    text-transform: uppercase; letter-spacing: 1px; white-space: nowrap;
  }
</style>
</head>
<body>
<main class="canvas">
  <article class="business-card">
    <svg class="card-shapes" viewBox="0 0 1000 572" aria-hidden="true">
      <defs>
        <linearGradient id="redPanelFill" x1="0" y1="0" x2="1" y2="1">
          <stop offset="0" stop-color="#e83340"/>
          <stop offset="1" stop-color="#c81d2b"/>
        </linearGradient>
      </defs>
      <path class="red-panel" d="M0 0 H600 Q470 230 470 572 H0 Z" fill="url(#redPanelFill)"/>
      <path class="black-swoosh" d="M612 0 H675 Q535 150 490 360 Q520 140 612 0 Z" fill="var(--swoosh-black)"/>
    </svg>

    <section class="contact-panel">
      <h1 class="person-name">Alex Sample</h1>
      <p class="person-title">Managing Director</p>
      <address class="postal-address">000, 1st Floor, Sample Plaza<br>Placeholder Road</address>
      <ul class="contact-list">
        <li class="contact-item">
          <svg class="contact-icon" viewBox="0 0 24 24"><path d="M6.6 10.8a15.1 15.1 0 0 0 6.6 6.6l2.2-2.2a1 1 0 0 1 1-.25 11.4 11.4 0 0 0 3.6.57 1 1 0 0 1 1 1V20a1 1 0 0 1-1 1A17 17 0 0 1 3 4a1 1 0 0 1 1-1h3.5a1 1 0 0 1 1 1c0 1.25.2 2.45.57 3.6a1 1 0 0 1-.25 1z"/></svg>
          <span>000 555 0100</span>
        </li>
        <li class="contact-item">
          <svg class="contact-icon" viewBox="0 0 24 24"><path d="M7 1h10a2 2 0 0 1 2 2v18a2 2 0 0 1-2 2H7a2 2 0 0 1-2-2V3a2 2 0 0 1 2-2zm0 3v14h10V4zm5 15.2a1.2 1.2 0 1 0 0 2.4 1.2 1.2 0 0 0 0-2.4z"/></svg>
          <span>000 555 0101</span>
        </li>
        <li class="contact-item">
          <svg class="contact-icon" viewBox="0 0 24 24"><path d="M2 5h20v14H2zm2 2v.5l8 5 8-5V7zm0 2.8V17h16V9.8l-8 5z"/></svg>
          <span>name@example.com</span>
        </li>
        <li class="contact-item">
          <svg class="contact-icon" viewBox="0 0 24 24"><path d="M12 2a10 10 0 1 0 0 20 10 10 0 0 0 0-20zm6.9 6h-3a15 15 0 0 0-1.3-3.6A8 8 0 0 1 18.9 8zM12 4c.8 1.2 1.5 2.5 1.9 4h-3.8c.4-1.5 1.1-2.8 1.9-4zM4.3 14a8 8 0 0 1 0-4h3.4a16 16 0 0 0 0 4zm.8 2h3a15 15 0 0 0 1.3 3.6A8 8 0 0 1 5.1 16zm3-8h-3a8 8 0 0 1 4.3-3.6A15 15 0 0 0 8.1 8zM12 20c-.8-1.2-1.5-2.5-1.9-4h3.8c-.4 1.5-1.1 2.8-1.9 4zm2.3-6H9.7a14 14 0 0 1 0-4h4.6a14 14 0 0 1 0 4zm.3 5.6a15 15 0 0 0 1.3-3.6h3a8 8 0 0 1-4.3 3.6zm1.7-5.6a16 16 0 0 0 0-4h3.4a8 8 0 0 1 0 4z"/></svg>
          <span>www.example.com</span>
        </li>
      </ul>
    </section>

    <div class="brand-lockup">
      <span class="brand-square" aria-hidden="true"></span>
      <span class="brand-name">Pike Hauling</span>
    </div>
  </article>
</main>
</body>
</html>
```